Retail Jewelry Business Card Design Project

We are in need of a new business card design for a retail jewelry store. This store is in the business of fine jewelry including but not specific to bridal jewelry, diamonds, designer jewelry and watches.

This store has been in business for 20 years but continues to strive for a modern professional appeal. The main colors use for this business are a royal blue, white and silver.

Target Market(s)

Target market is ages 18-50

Industry/Entity Type

Jewelry

Requirements
Must have
• Sales Person Name
Sales Person Email Address

Store Address
Store Phone
Website

Standard business card size. No odd shapes or sizes.
Nice to have
• Overall modern feel for card.

We have thought that a design with a nice feature of the logo on the back of the card would be nice but open to ideas.
Should not have
• No specific images of jewelry should be used.

```html
<!DOCTYPE html>
<html lang="en">
<head>
<meta charset="utf-8">
<title>Marcus Vale Fine Jewelry – Business Card</title>
<link rel="stylesheet" href="https://fonts.googleapis.com/css2?family=Cormorant+Garamond:ital,wght@0,600;1,500&display=swap">
<style>
  :root {
    --page: #ffffff;
    --royal: #13097a;
    --royal-deep: #2e1d8e;
    --royal-ink: #2a0f8a;
    --glow: #ffffff;
    --silver: #8d8d95;
    --frame: #5b6182;
    --text-light: #ffffff;
  }
  * { margin: 0; padding: 0; box-sizing: border-box; }
  html, body {
    width: 1200px;
    height: 677px;
    overflow: hidden;
    background: var(--page);
  }
  .canvas {
    position: relative;
    width: 1200px;
    height: 677px;
  }
  .card {
    position: absolute;
    overflow: hidden;
  }
  .card--front {
    left: 100px; top: 226px; width: 494px; height: 283px;
    background: radial-gradient(ellipse 230px 190px at 245px 110px,
      var(--glow) 0%, #c9bfe3 35%, #7a63b8 70%, var(--royal-deep) 100%);
  }
  .card--back {
    left: 600px; top: 227px; width: 496px; height: 284px;
    background: var(--royal);
  }
  .brand {
    position: absolute;
    font-family: "Cormorant Garamond", Georgia, serif;
    font-weight: 600;
    font-style: normal;
    text-align: center;
    line-height: 1;
  }
  .brand__name { display: block; }
  .brand__tag { display: block; letter-spacing: 2px; text-transform: uppercase; }
  .card--front .brand {
    left: 0; width: 494px; top: 82px;
    color: var(--royal-ink);
  }
  .card--front .brand__name { font-size: 58px; }
  .card--front .brand__tag { font-size: 21px; margin-top: 22px; }
  .card--back .brand {
    left: 50px; width: 240px; top: 22px;
    color: var(--silver);
  }
  .card--back .brand__name { font-size: 38px; }
  .card--back .brand__tag { font-size: 15px; margin-top: 9px; }
  .frame { position: absolute; left: 0; top: 0; }
  .contact {
    position: absolute;
    font-family: "Cormorant Garamond", Georgia, serif;
    font-style: italic;
    font-weight: 500;
    color: var(--text-light);
    font-size: 21px;
    line-height: 1;
    white-space: nowrap;
  }
  .contact--name { left: 248px; top: 95px; }
  .contact--street { left: 248px; top: 133px; }
  .contact--city { left: 248px; top: 162px; }
  .contact--email { left: 193px; top: 194px; display: flex; align-items: center; gap: 6px; }
  .contact--web { left: 86px; width: 305px; top: 245px; text-align: center; }
</style>
</head>
<body>
<main class="canvas">
  <section class="card card--front" aria-label="Card front">
    <div class="brand">
      <span class="brand__name">Marcus Vale</span>
      <span class="brand__tag">Fine Jewelry</span>
    </div>
  </section>

  <section class="card card--back" aria-label="Card back">
    <div class="brand">
      <span class="brand__name">Marcus Vale</span>
      <span class="brand__tag">Fine Jewelry</span>
    </div>

    <svg class="frame" width="496" height="284" viewBox="0 0 496 284" aria-hidden="true">
      <g stroke="var(--frame)" stroke-width="5" fill="none">
        <line x1="12" y1="125" x2="486" y2="125"/>
        <line x1="12" y1="228" x2="486" y2="228"/>
        <line x1="25" y1="113" x2="25" y2="240"/>
        <line x1="470" y1="113" x2="470" y2="240"/>
      </g>
      <rect x="86" y="238" width="305" height="30" rx="14" ry="14"
            fill="none" stroke="var(--frame)" stroke-width="2.5"/>
    </svg>

    <p class="contact contact--name">Marcus Vale Hartwell</p>
    <p class="contact contact--street">2280 Linden Avenue</p>
    <p class="contact contact--city">Port Elmira, FL 32955</p>
    <p class="contact contact--email">
      <svg width="18" height="14" viewBox="0 0 18 14" aria-hidden="true">
        <rect x="1" y="1" width="16" height="12" fill="#ffffff" stroke="#c8c8d0"/>
        <polyline points="1,1 9,8 17,1" fill="none" stroke="#9a9aa5" stroke-width="1.2"/>
      </svg>
      marcus@marcusvalejewelry.com
    </p>
    <p class="contact contact--web">www.marcusvalejewelry.com</p>
  </section>
</main>
</body>
</html>
```